RV Park - Advertising RV Park using Billboard 12 ft wide by 6 ft tall size

We need a sign for a relatively new RV Park called Bramblewood of Carver RV Park at 2745 Danbury Road, Murphy , NC. The sign should include our web address and phone number. bramblewoodcarverrv.example, 555-314-2967. We would like to see designs that include nice color and no tacky cartoons. Final design should communicate a nice and safe RV Park. We would also like to include quick directions - Just Ahead! Left on Kestrel Rd then left on Danbury Rd. (A nice motor home or RV representation may be nice but not mandatory to be included.) Classic but eye catching design. Sign is 12 ft wide by 6 ft tall in size. Will likely be vinyl printed.

```html
<!DOCTYPE html>
<html lang="en">
<head>
<meta charset="utf-8">
<title>Bramblewood of Carver RV Park – Billboard</title>
<link rel="stylesheet" href="https://fonts.googleapis.com/css2?family=Oswald:wght@500;700&display=swap">
<style>
  :root {
    --page-bg: #eef0f2;
    --board-red: #6e0f16;
    --board-red-deep: #4a070c;
    --skyline-tone: #5a0b12;
    --headline-white: #ffffff;
    --accent-yellow: #f6d21a;
    --direction-box: #ffffff;
    --direction-text: #2a0a0c;
  }
  * { margin: 0; padding: 0; box-sizing: border-box; }
  html, body {
    width: 816px;
    height: 1200px;
    overflow: hidden;
    background: var(--page-bg);
  }
  .canvas {
    width: 816px;
    height: 1200px;
    display: flex;
    align-items: center;
    justify-content: center;
  }
  .billboard {
    position: relative;
    width: 760px;
    height: 380px;
    background: radial-gradient(ellipse at 50% 40%, var(--board-red) 0%, var(--board-red-deep) 100%);
    overflow: hidden;
    box-shadow: 0 6px 18px rgba(0,0,0,0.25);
    font-family: 'Oswald', sans-serif;
    text-align: center;
  }
  .skyline-backdrop {
    position: absolute;
    left: 0; right: 0; bottom: 0;
    height: 170px;
    background: linear-gradient(to top, var(--skyline-tone) 0%, rgba(90,11,18,0.55) 55%, rgba(90,11,18,0) 100%);
  }
  .sign-content {
    position: relative;
    padding-top: 26px;
    display: flex;
    flex-direction: column;
    align-items: center;
  }
  .park-name {
    color: var(--headline-white);
    font-weight: 700;
    font-size: 50px;
    line-height: 1;
    letter-spacing: 0.5px;
  }
  .park-type {
    color: var(--accent-yellow);
    font-weight: 700;
    font-size: 112px;
    line-height: 1;
    margin-top: 4px;
  }
  .web-address {
    color: var(--headline-white);
    font-weight: 700;
    font-size: 27px;
    line-height: 1;
    margin-top: 6px;
    letter-spacing: 0.5px;
  }
  .directions {
    display: flex;
    align-items: center;
    gap: 12px;
    margin-top: 14px;
  }
  .just-ahead {
    color: var(--accent-yellow);
    font-weight: 700;
    font-size: 26px;
    line-height: 1;
  }
  .route {
    background: var(--direction-box);
    color: var(--direction-text);
    font-weight: 500;
    font-size: 22px;
    line-height: 1;
    padding: 5px 10px;
  }
  .phone {
    color: var(--headline-white);
    font-weight: 700;
    font-size: 48px;
    line-height: 1;
    margin-top: 14px;
    letter-spacing: 1px;
  }
</style>
</head>
<body>
  <main class="canvas">
    <section class="billboard">
      <div class="skyline-backdrop" role="img" aria-label="Faint city skyline silhouette along the bottom of the sign"></div>
      <div class="sign-content">
        <h1 class="park-name">BRAMBLEWOOD OF CARVER</h1>
        <p class="park-type">RV PARK</p>
        <p class="web-address">www.bramblewoodcarverrv.example</p>
        <div class="directions">
          <span class="just-ahead">JUST AHEAD</span>
          <span class="route">Left on Kestrel Rd, then Left on Danbury</span>
        </div>
        <p class="phone">555-314-2967</p>
      </div>
    </section>
  </main>
</body>
</html>
```